A Label for an ECO Friendly Spirit Company

Design a label which can be used for vodka and gin (London Dry Gin). It should be Square type Like the Shape File you see in the uploads. VORK means Local Eco friendly Authentic and Fair. We want a cool and slim label that calls for eco-friendly. We want to use it for our premium
Vodka and our London Dry Gin. Please use the logo and design it in Square Type.

40%vol, 700ml

Target Market(s)

spirits and events

Industry/Entity Type

SPIRITS

Colors
00AB8E
00BBA5
67D7C9
C6EFE9
E9F9F6
59FF00
82FF00
B8FF75
E3FFCB
F4FFEA

Requirements
Must have
• Logo from VORK, Squaee Shape

```html
<!DOCTYPE html>
<html lang="en">
<head>
<meta charset="utf-8">
<title>VORK Spirits Labels</title>
<link rel="stylesheet" href="https://fonts.googleapis.com/css2?family=Montserrat:wght@300;400;500;600;700&family=Great+Vibes&display=swap">
<style>
  :root {
    --page-bg: #ffffff;
    --label-light: #d3efe8;
    --label-mid: #8fcfc3;
    --label-teal: #3fa59c;
    --label-deep: #1d6f74;
    --brand-green: #1aa283;
    --mark-lime: #8cc63f;
    --ink-dark: #1f3b2a;
    --ink-soft: #233a2c;
    --white: #ffffff;
  }
  * { margin: 0; padding: 0; box-sizing: border-box; }
  html, body { width: 958px; height: 1200px; overflow: hidden; background: var(--page-bg); }
  .canvas { position: relative; width: 958px; height: 1200px; }

  .label {
    position: absolute;
    width: 374px;
    height: 374px;
    clip-path: polygon(50% 0, 100% 50%, 50% 100%, 0 50%);
    background:
      radial-gradient(ellipse at 85% 75%, rgba(110, 200, 210, 0.55), transparent 45%),
      linear-gradient(160deg, var(--label-light) 0%, var(--label-mid) 40%, var(--label-teal) 70%, var(--label-deep) 100%);
    font-family: "Montserrat", sans-serif;
  }
  .label--vodka { left: 54px; top: 121px; }
  .label--gin { left: 538px; top: 725px; }

  .label > * { position: absolute; left: 0; right: 0; text-align: center; line-height: 1; }

  .brand-mark {
    left: 50%; right: auto;
    width: 42px; height: 42px;
    margin-left: -21px;
    top: 56px;
    background: var(--mark-lime);
    border-radius: 6px;
  }
  .brand-name {
    top: 102px;
    font-weight: 600;
    font-size: 32px;
    letter-spacing: 0.5px;
    color: var(--brand-green);
  }
  .tier {
    left: 50%; right: auto;
    transform: translateX(-50%);
    padding: 3px 15px 2px;
    background: var(--ink-dark);
    color: var(--white);
    font-weight: 700;
    font-size: 10px;
    letter-spacing: 0.4px;
    clip-path: polygon(0 0, 100% 0, 94% 50%, 100% 100%, 0 100%, 6% 50%);
  }
  .label--vodka .tier { top: 149px; }
  .label--gin .tier { top: 146px; }

  .style-line {
    top: 166px;
    font-weight: 300;
    font-size: 13px;
    letter-spacing: 1px;
    color: var(--ink-soft);
  }
  .product-name {
    font-family: "Great Vibes", cursive;
    color: var(--ink-dark);
  }
  .label--vodka .product-name { top: 174px; font-size: 64px; }
  .label--gin .product-name { top: 190px; font-size: 48px; }

  .strength {
    font-weight: 500;
    font-size: 13px;
    color: var(--ink-soft);
  }
  .label--vodka .strength { top: 232px; }
  .label--gin .strength { top: 248px; }

  .claim {
    font-weight: 700;
    font-size: 11px;
    color: var(--white);
  }
  .label--vodka .claim { top: 260px; }
  .label--gin .claim { top: 270px; }

  .volume {
    top: 304px;
    font-weight: 700;
    font-size: 12px;
    color: var(--white);
  }
  .volume span { display: block; margin-top: 3px; font-weight: 500; font-size: 10px; }
</style>
</head>
<body>
<main class="canvas">
  <section class="label label--vodka" aria-label="VORK Premium Vodka label">
    <div class="brand-mark"></div>
    <div class="brand-name">VORK</div>
    <div class="tier">PREMIUM</div>
    <div class="product-name">Vodka</div>
    <div class="strength">40% VOL</div>
    <div class="claim">ECO FRIENDLY</div>
    <div class="volume">700<span>ml</span></div>
  </section>

  <section class="label label--gin" aria-label="VORK Premium London Dry Gin label">
    <div class="brand-mark"></div>
    <div class="brand-name">VORK</div>
    <div class="tier">PREMIUM</div>
    <div class="style-line">LONDON</div>
    <div class="product-name">Dry Gin</div>
    <div class="strength">40% VOL</div>
    <div class="claim">ECO FRIENDLY</div>
    <div class="volume">700<span>ml</span></div>
  </section>
</main>
</body>
</html>
```